Envelope and Stationary

I need an envelope and stationary package for my non-profit. I need to be able to download these, print, and use.

I am attached the logos, color files, and information I want on envelope and stationary.

The letter must have room on the left margin to put the list of names, Board Members, etc... I will attach a sample.

What I am looking for is to jazz this up a little bit. The Tobin Vale Children's Foundation is promotes physical fitness in children through after school programs.

Once this project is done, I need a powerpoint template, business cards, and many other pieces.

Please help me make my envelopes and letterhead standout from everyone else.

Target Market(s)

Donors, Community citizens, and prospective partners.

Industry/Entity Type

Fitness

Requirements
Must have
• 1) Logo - see attached
2) Mission Statement - "The MISSION of the TOBIN VALE FOUNDATION is to provide after school enrichment, health, and fitness programs in a safe and nurturing environment."
3) Contact information
4) Space on left Margin for Board of Directors (this space will be available for edits to add/subtract names).

5) See sample letter head: The logo and address is too small and barely visible.

6) PO BOX 315927 * Alder Bay, Coastland 30418
Phone: 877-(TVF)-2815
Email: community@tvfyouth.org
Web: www.tvfyouth.org
Nice to have
• Logo and colors have some feel or scheme across top. Something that makes the letterhead and envelope stand out.

```html
<!DOCTYPE html>
<html lang="en">
<head>
<meta charset="utf-8">
<title>Tobin Vale Foundation — Letterhead and Envelope</title>
<link rel="stylesheet" href="https://fonts.googleapis.com/css2?family=Didact+Gothic&display=swap">
<style>
  :root {
    --page-bg: #f1f1f1;
    --paper: #ffffff;
    --brand-blue: #1f74bd;
    --brand-red: #c01f2f;
    --text-blue: #2a79c2;
    --deco-blue: #c0dbee;
    --deco-pink: #ecc3c9;
    --deco-blue-soft: #dce9f4;
    --deco-pink-soft: #f2d9dd;
    --window-line: #b9b9b9;
  }
  * { margin: 0; padding: 0; box-sizing: border-box; }
  html, body {
    width: 1200px; height: 1000px; overflow: hidden;
    background: var(--page-bg);
    font-family: "Didact Gothic", "Helvetica Neue", Arial, sans-serif;
  }
  .canvas { position: relative; width: 1200px; height: 1000px; }

  .sheet { position: absolute; background: var(--paper); overflow: hidden; }
  .letterhead { left: 68px; top: 151px; width: 495px; height: 700px; }
  .envelope { left: 606px; top: 262px; width: 519px; height: 260px; }

  .brand { position: absolute; display: flex; align-items: center; gap: 5px; }
  .brand-square { width: 10px; height: 10px; background: var(--brand-red); flex: none; }
  .brand-name {
    color: var(--brand-blue); font-size: 12px; letter-spacing: 0.2px;
    white-space: nowrap; line-height: 1;
  }
  .letterhead .brand { left: 31px; top: 42px; }
  .envelope .brand { left: 21px; top: 43px; }

  .contact {
    position: absolute; color: var(--text-blue); font-style: normal;
    font-size: 7.6px; line-height: 9px; letter-spacing: 0.3px; white-space: nowrap;
  }
  .letterhead .contact { left: 130px; top: 25px; }
  .envelope .contact { left: 120px; top: 27px; }

  .rule { position: absolute; height: 5px; background: var(--brand-red); right: 0; }
  .letterhead .rule { left: 130px; top: 68px; }
  .envelope .rule { left: 120px; top: 71px; }

  .monogram-field { position: absolute; right: 0; bottom: 0; border-radius: 60px 0 0 0; }
  .letterhead .monogram-field {
    width: 296px; height: 144px;
    background: linear-gradient(90deg, var(--deco-blue) 0%, var(--deco-blue) 68%, var(--deco-pink) 100%);
  }
  .envelope .monogram-field {
    width: 339px; height: 165px;
    background: linear-gradient(90deg, var(--deco-blue-soft) 0%, var(--deco-blue-soft) 68%, var(--deco-pink-soft) 100%);
  }

  .address-window {
    position: absolute; left: 273px; top: 124px; width: 212px; height: 99px;
    border: 1px dashed var(--window-line); border-radius: 6px;
  }
</style>
</head>
<body>
<main class="canvas">

  <section class="sheet letterhead" aria-label="Letterhead">
    <div class="brand">
      <span class="brand-square"></span>
      <span class="brand-name">TOBIN VALE</span>
    </div>
    <address class="contact">
      PO BOX 315927 * Alder Bay, Coastland 30418<br>
      Phone: 877-(TVF)-2815<br>
      Email: community@tvfyouth.org<br>
      Web: www.tvfyouth.org
    </address>
    <div class="rule"></div>
    <div class="monogram-field" role="img" aria-label="Large faint brand monogram in light blue and pink"></div>
  </section>

  <section class="sheet envelope" aria-label="Envelope">
    <div class="brand">
      <span class="brand-square"></span>
      <span class="brand-name">TOBIN VALE</span>
    </div>
    <address class="contact">
      PO BOX 315927 * Alder Bay, Coastland 30418<br>
      Phone: 877-(TVF)-2815<br>
      Email: community@tvfyouth.org<br>
      Web: www.tvfyouth.org
    </address>
    <div class="rule"></div>
    <div class="monogram-field" role="img" aria-label="Large faint brand monogram in pale blue and pink"></div>
    <div class="address-window"></div>
  </section>

</main>
</body>
</html>
```